A farm is looking for the unified design for the bags' and bottles' labels in their organic produ...

We are a farm that deals with the production and sale of the organic seeds and oils. From the seed programme, we offer the organic flax, sunflower, hemp and pumpkin seeds. In our program, the organic unrefined cold-pressed hemp, linseed and sunflower oil and cold-pressed pumpkin oil can be found.
Design wise, we want to unify our sales programme with a unique organic look of bottle labels containing organic oils and labels for paper bags containing seeds.
We intend to keep the appearance of the exiting logotype (refer to the logotype provided in the enclosed PDF file). Regarding the colours, our products should be separated by a colour scheme (hemp, flax, pumpkin seeds, sunflower, etc.). The label material should be the same for the bags and the bottles. If possible, we would like to utilize the ecological paper, together with the option of applying the labels using the organic glue (starch, etc.). Also, the possibility of the eventual later printing directly onto the packaging (paper bags and bottles) must be considered and envisioned.
Additionally, there should be space on the label for the written title of the product (for example, »BIO pumpkin seeds«) and some space for short indications, markings and data in the corners of the label. You can also include an image that will indicate the contents of the bag/bottle.
We will appreciate all your contributions.

IN DOMESTIC LANGUAGE:
Smo kmetija, ki se ukvarja s pridelavo in prodajo ekoloških semen in olj. Iz programa semen nudimo BIO lanena, sončnična, konopljina in bučna semena. V našem programu so BIO nerafinirano hladno stiskano konopljino, laneno ter sončnično olje in hladno stiskano bučno olje.
Želimo oblikovno poenotiti naš prodajni program z enotnim EKO videzom etiket za steklenice z BIO olji in etiket za papirnate vrečke z semeni.
Ohraniti nameravamo videz obstoječega logotipa (glej logotip v priloženi PDF datoteki). Barvno je treba ločiti proizvode po barvni shemi (konoplja, lan, bučno seme, sončnica …). Material etiket naj bo enak za vrečke in steklenice. Po možnosti naj gre za ekološki papir, pa tudi možnost nanosa etiket z ekološkim lepilom (škrob …). Predvideti je treba tudi možen kasnejši tisk neposredno na embalažo (papirnate vrečke ter steklenice).
Prav tako naj bo na etiketi prostor za napis naslova izdelka (na primer »BIO bučno seme«) in po robovih nekaj prostora za krajše navedbe, označbe ter podatke, vključena pa je lahko tudi slika, ki nakazuje na vsebino vrečke/steklenice.
Najlepša hvala že vnaprej za vaše prispevke.

```html
<!DOCTYPE html>
<html lang="en">
<head>
<meta charset="utf-8">
<title>Bio Pumpkin Seeds Label</title>
<link href="https://fonts.googleapis.com/css2?family=Barlow:wght@300;400;700&display=swap" rel="stylesheet">
<style>
  :root {
    --ink: #262626;
    --seed-dark: #2a2a27;
    --amber: #f6a623;
    --white: #ffffff;
    --badge-tone: #f0f0ea;
    --badge-edge: #1f6b3a;
  }
  html, body {
    margin: 0;
    padding: 0;
    width: 1200px;
    height: 1006px;
    overflow: hidden;
    background: var(--ink);
  }
  .label {
    display: block;
    width: 1200px;
    height: 1006px;
    font-family: "Barlow", Arial, sans-serif;
  }
  .logo-text { font-weight: 300; font-size: 26px; fill: #e6e6e6; letter-spacing: 0.5px; }
  .title-main { font-weight: 700; font-size: 230px; fill: var(--white); }
  .title-sub { font-weight: 700; font-size: 68px; fill: var(--white); }
  .claim { font-weight: 300; font-size: 37px; fill: var(--white); }
  .net-weight { font-weight: 400; font-size: 14px; fill: var(--ink); }
</style>
</head>
<body>
<svg class="label" viewBox="0 0 1200 1006" xmlns="http://www.w3.org/2000/svg">
  <defs>
    <radialGradient id="warm-field" cx="50%" cy="48%" r="62%">
      <stop offset="0%" stop-color="#f9e53a"/>
      <stop offset="50%" stop-color="#f7cf2b"/>
      <stop offset="82%" stop-color="#f5a323"/>
      <stop offset="100%" stop-color="#f0841c"/>
    </radialGradient>
    <clipPath id="seed-circle">
      <circle cx="600" cy="574" r="312"/>
    </clipPath>
  </defs>

  <!-- Label sheet -->
  <rect class="label-sheet" role="img" aria-label="Warm orange and yellow background with halftone dot pattern" x="130" y="99" width="940" height="807" fill="url(#warm-field)"/>

  <!-- Logo band -->
  <rect class="logo-band" x="474" y="99" width="252" height="200" fill="var(--ink)"/>
  <text class="logo-text" x="600" y="188" text-anchor="middle">YOUR LOGO</text>
  <text class="logo-text" x="600" y="224" text-anchor="middle">HERE</text>

  <!-- Product window -->
  <circle class="window-ring" cx="600" cy="574" r="320" fill="var(--amber)"/>
  <g clip-path="url(#seed-circle)">
    <rect class="seed-photo" role="img" aria-label="Close-up photograph of pumpkin seeds" x="280" y="254" width="640" height="640" fill="var(--seed-dark)"/>
    <rect class="net-band" x="280" y="816" width="640" height="46" fill="var(--white)"/>
  </g>

  <text class="title-main" x="602" y="524" text-anchor="middle">BIO</text>
  <text class="title-sub" x="600" y="598" text-anchor="middle">PUMPKIN SEEDS</text>

  <text class="claim" x="606" y="678" text-anchor="middle">• 100 % PURE</text>
  <line class="claim-rule" x1="464" y1="686" x2="736" y2="686" stroke="var(--white)" stroke-width="2.5"/>
  <text class="claim" x="596" y="726" text-anchor="middle">• UNREFIEND</text>
  <line class="claim-rule" x1="464" y1="734" x2="736" y2="734" stroke="var(--white)" stroke-width="2.5"/>
  <text class="claim" x="600" y="774" text-anchor="middle">• COLD-PRESSED</text>

  <text class="net-weight" x="600" y="843" text-anchor="middle">NET WT. 7 OZ. (50 ML)</text>

  <!-- Certification badge placeholder -->
  <circle class="cert-badge" role="img" aria-label="Organic certification badge" cx="980" cy="816" r="56" fill="var(--badge-tone)" stroke="var(--badge-edge)" stroke-width="3"/>
</svg>
</body>
</html>
```